BRMSC redesign and update stationary bc envelopes.

Stationary, Envelopes, Brochures, Business Card. Need to add second surgeon and two other offices. I need everything to match. I am a oral & maxillofacial surgeon.
Additional surgeon and three office addresses.
Tae Woo Park, DMD, MD, INC

3178 Silver Meadow Boulevard
Ridgefield Hills, CA 95718

612 Lorel Lane, Suite 208
Lakemont, CA. 95644

2375 Birch Avenue, Suite 314
Brookvale, CA. 95410
Updates

Logo design uploaded. Zapfino Extra/Adobe Garamond/Palatino are fonts used before. Not sure what is on exisiting stationary.

Target Market(s)

Referral dentist and sometimes patients. I am a oral & Maxillofacial surgeon.

Industry/Entity Type

Dental Clinic

Font styles to use
Serif
Script

Requirements
Must have
• Color of existing stationary. Update is possible.
Nice to have
• Conservative/modern
Should not have
• Playful

```html
<!DOCTYPE html>
<html lang="en">
<head>
<meta charset="utf-8">
<title>BRMSC Letterhead</title>
<link rel="stylesheet" href="https://fonts.googleapis.com/css2?family=Crimson+Pro:ital,wght@0,400;0,500;1,400;1,600&display=swap">
<style>
  :root {
    --backdrop: #e9e6df;
    --paper: #fdfbf0;
    --ink-brown: #5a4337;
    --band-brown: #664c40;
    --leaf-green: #6b8e23;
    --band-text: #f2ebe3;
  }
  * { box-sizing: border-box; margin: 0; padding: 0; }
  html, body {
    width: 1091px;
    height: 1200px;
    overflow: hidden;
    background: var(--backdrop);
  }
  .letterhead {
    position: absolute;
    left: 106px;
    top: 30px;
    width: 880px;
    height: 1140px;
    background: var(--paper);
    box-shadow: 0 2px 10px rgba(0,0,0,0.15);
    font-family: "Crimson Pro", "Palatino Linotype", serif;
    color: var(--ink-brown);
  }
  .brand {
    position: absolute;
    left: 70px;
    top: 74px;
    display: flex;
    align-items: center;
    gap: 14px;
  }
  .brand-mark {
    width: 18px;
    height: 18px;
    border-radius: 50%;
    background: var(--leaf-green);
  }
  .brand-name {
    font-size: 46px;
    font-weight: 500;
    letter-spacing: 3px;
    color: var(--ink-brown);
  }
  .contact-block {
    position: absolute;
    right: 60px;
    top: 48px;
    text-align: right;
    font-style: normal;
    font-size: 15px;
    line-height: 1.15;
  }
  .office { margin-bottom: 4px; }
  .office-divider {
    display: block;
    width: 5px;
    height: 5px;
    margin: 0 0 6px auto;
    background: var(--leaf-green);
  }
  .phone-line { margin-top: 4px; }
  .phone-label {
    font-style: italic;
    font-weight: 600;
    color: var(--leaf-green);
    margin-right: 3px;
  }
  .email { margin-top: 2px; }
  .footer-rule {
    position: absolute;
    left: 0;
    right: 0;
    bottom: 104px;
    height: 4px;
    background: var(--leaf-green);
  }
  .footer-band {
    position: absolute;
    left: 0;
    right: 0;
    bottom: 0;
    height: 96px;
    background: var(--band-brown);
    display: flex;
    align-items: center;
    justify-content: center;
  }
  .web-address {
    font-style: italic;
    font-size: 26px;
    letter-spacing: 7px;
    color: var(--band-text);
  }
</style>
</head>
<body>
  <main class="letterhead">
    <header class="brand">
      <span class="brand-mark"></span>
      <span class="brand-name">BRMSC</span>
    </header>

    <address class="contact-block">
      <p class="office">2375 Birch Avenue, Suite 314<br>Brookvale, CA. 95410</p>
      <span class="office-divider"></span>
      <p class="office">3178 Silver Meadow Boulevard<br>Ridgefield Hills, CA 95718</p>
      <span class="office-divider"></span>
      <p class="office">612 Lorel Lane, Suite 208<br>Lakemont, CA. 95644</p>
      <span class="office-divider"></span>
      <p class="phone-line"><span class="phone-label">Tel</span>916.555.0142</p>
      <p><span class="phone-label">Fax</span>916.555.0187</p>
      <p class="email">drpark@silvermeadoworalsurgery.com</p>
    </address>

    <div class="footer-rule"></div>
    <footer class="footer-band">
      <p class="web-address">www.silvermeadoworalsurgery.com</p>
    </footer>
  </main>
</body>
</html>
```